Riverline Estate Holdings Co.

We need a logo and business card design for a Hong Kong based real estate company, KDT Land. We are want the brand to reflect the owners forward thinking, creative, and trend setting projects, while also reflecting a sense of security and strength. We invest in industrial properties which we convert to co-living or co-working spaces. KDT stands for Greater Bay Area which is the region around southern China including HK, Macau, and 9 other Chinese cities...made up of approx. 68 million people. There are massive infrastructure projects including the bridge to Macau and high-speed rail to SZ and the bridge connecting SZ and Zhongshan.

Target Market(s)

Chinese and western retail investors, as well as institutional investors

Industry/Entity Type

Real Estate Development

Contact Information for Business Card

Owen Tallis
CEO
owen@kdtland-hq.com
M + 852 9416 2057
F + 852 3582 0400
Suite 2207, The Meridale, 41 Larchmont Rd., Central, Hong Kong

Logo Text

kdt land (company name) lifestyle property development (underneath)

Colors

Designer to choose colors to be used in the design.

Requirements
Must have
• Details listed above. One side should include the logo and company name...kdt land in modern, hip styling with "lifestyle property development"
Nice to have
• Could be a Black card, with metallic purple "kdt" and white "land"...but open great design ideas
Should not have
• boring and traditional layout

```html
<!DOCTYPE html>
<html lang="en">
<head>
<meta charset="utf-8">
<title>KDT Land — Business Card</title>
<link href="https://fonts.googleapis.com/css2?family=Montserrat:wght@500;600&family=Open+Sans:wght@400&display=swap" rel="stylesheet">
<style>
  :root {
    --backdrop: #2b2b2d;
    --card: #1f1f21;
    --card-edge: #2a2a2c;
    --purple: #7b4fc0;
    --purple-soft: #9a7ad0;
    --text: #e6e6ea;
    --text-muted: #c9c9cf;
  }
  * { margin: 0; padding: 0; box-sizing: border-box; }
  html, body { width: 1200px; height: 716px; overflow: hidden; }
  body {
    background: var(--backdrop);
    font-family: "Open Sans", sans-serif;
    color: var(--text);
    position: relative;
  }
  .card {
    position: absolute;
    width: 500px;
    height: 286px;
    background: var(--card);
    border: 1px solid var(--card-edge);
    border-radius: 3px;
    box-shadow: 0 12px 30px rgba(0,0,0,0.45);
  }
  .card--front { left: 60px; top: 50px; }
  .card--back { left: 620px; top: 210px; }

  .brand {
    display: flex;
    align-items: center;
    gap: 12px;
    white-space: nowrap;
  }
  .brand__square {
    flex: none;
    width: 34px; height: 34px;
    background: var(--purple);
  }
  .brand__text { display: flex; flex-direction: column; }
  .brand__name {
    font-family: "Montserrat", sans-serif;
    font-weight: 600;
    font-size: 30px;
    line-height: 1.1;
    letter-spacing: 6px;
    color: var(--text);
  }
  .brand__tagline {
    margin-top: 4px;
    font-family: "Montserrat", sans-serif;
    font-weight: 500;
    font-size: 9px;
    letter-spacing: 2px;
    text-transform: uppercase;
    color: var(--purple-soft);
  }

  .card--front .brand {
    position: absolute;
    left: 0; right: 0; top: 88px;
    justify-content: center;
  }
  .front__web {
    position: absolute;
    left: 0; right: 0; top: 184px;
    text-align: center;
    font-size: 13px;
    letter-spacing: 2.5px;
    color: var(--purple-soft);
  }

  .person { position: absolute; left: 36px; top: 32px; }
  .person__name {
    font-family: "Montserrat", sans-serif;
    font-weight: 600;
    font-size: 19px;
    color: var(--text);
  }
  .person__role {
    display: inline-block;
    margin-top: 2px;
    font-size: 12px;
    color: var(--purple-soft);
    padding-bottom: 3px;
    border-bottom: 1px solid var(--purple-soft);
  }

  .contacts {
    position: absolute; left: 36px; top: 110px;
    list-style: none;
  }
  .contacts li {
    display: flex; align-items: center; gap: 10px;
    font-size: 13px; color: var(--text-muted);
    margin-bottom: 9px;
  }
  .contacts svg { width: 13px; height: 13px; fill: var(--text-muted); }

  .address {
    position: absolute; left: 36px; top: 222px;
    display: flex; align-items: center; gap: 10px;
    font-size: 12.5px; color: var(--text-muted);
  }
  .address svg { width: 12px; height: 14px; fill: var(--text-muted); }

  .card--back .brand {
    position: absolute; right: 30px; top: 124px;
    gap: 10px;
  }
  .card--back .brand__name { font-size: 22px; letter-spacing: 4px; }
  .card--back .brand__tagline { font-size: 7px; letter-spacing: 1.4px; }
  .card--back .brand__square { width: 28px; height: 28px; }

  .standalone-brand {
    position: absolute; left: 90px; top: 556px;
  }
  .standalone-brand .brand__square { width: 52px; height: 52px; }
  .standalone-brand .brand__name { font-size: 44px; letter-spacing: 9px; }
  .standalone-brand .brand__tagline { font-size: 12px; letter-spacing: 3px; }
</style>
</head>
<body>

  <section class="card card--front">
    <div class="brand">
      <span class="brand__square"></span>
      <span class="brand__text">
        <span class="brand__name">KDT LAND</span>
        <span class="brand__tagline">lifestyle property development</span>
      </span>
    </div>
    <p class="front__web">www.kdtland-hq.com</p>
  </section>

  <section class="card card--back">
    <div class="person">
      <h1 class="person__name">OWEN TALLIS</h1>
      <span class="person__role">CEO</span>
    </div>

    <ul class="contacts">
      <li>
        <svg viewBox="0 0 16 16"><path d="M1 3h14v10H1z M1 3l7 6 7-6" fill="none" stroke="#c9c9cf" stroke-width="1.5"/></svg>
        owen@kdtland-hq.com
      </li>
      <li>
        <svg viewBox="0 0 16 16"><rect x="4" y="1" width="8" height="14" rx="1.5" fill="none" stroke="#c9c9cf" stroke-width="1.5"/><circle cx="8" cy="12.5" r="0.9"/></svg>
        852 9416 2057
      </li>
      <li>
        <svg viewBox="0 0 16 16"><path d="M1 6c0-2 3-3 7-3s7 1 7 3v1h-3V5.5H4V7H1z M3 8h10l1 6H2z"/></svg>
        852 3582 0400
      </li>
    </ul>

    <p class="address">
      <svg viewBox="0 0 12 16"><path d="M6 0a6 6 0 0 0-6 6c0 4.5 6 10 6 10s6-5.5 6-10a6 6 0 0 0-6-6zm0 8.5A2.5 2.5 0 1 1 6 3.5a2.5 2.5 0 0 1 0 5z"/></svg>
      Suite 2207, The Meridale, 41 Larchmont Rd., Central, Hong Kong
    </p>

    <div class="brand">
      <span class="brand__square"></span>
      <span class="brand__text">
        <span class="brand__name">KDT LAND</span>
        <span class="brand__tagline">lifestyle property development</span>
      </span>
    </div>
  </section>

  <div class="brand standalone-brand">
    <span class="brand__square"></span>
    <span class="brand__text">
      <span class="brand__name">KDT LAND</span>
      <span class="brand__tagline">lifestyle property development</span>
    </span>
  </div>

</body>
</html>
```